Home Page Design (+50 More Pages To Winning Designer!)

We have a 50+ page website, but we're starting with the home page. The winning designer will get all 50+ pages to design as a 2nd project, so make sure you do your best!

SoarVane is in the private jet industry and needs a re-designed website.

We have created the structure for the website and content inside of Tavoni.io (THESE ARE ONLY ROUGH A.I. GENERATED WIREFRAMES AND DO NOT NEED TO BE FOLLOWED EXACTLY) - https://www.tavoni.io/app/project/P482915_qRuVwKsLm-DDtaHrYuop72XNc8fkoPzqlrhwDxHkaWm3Tq

Take the content from the 'Home Page' under the 'Wireframe' tab on the Tavoni.io link above, but feel free to re-design the page in a better way as these are only A.I. generated wireframes.

We want a DARK theme.... High quality, luxurious feel, greyscale colors. Attached is a brand guideline (BUT THIS IS NOT A 100% BRAND GUIDELINE, YOU CAN CHANGE COLORS AND FONTS AND MAKE CHANGES IF YOU HAVE BETTER IDEAS) and attached is our logo. We are also attaching some examples of other apps and websites to give you a guideline of what we're looking for for this design project.

The final design MUST communicate luxury using high-quality imagery of large cabin luxurious private jets.

ENTRIES THAT DO NOT FOLLOW THE PROJECT BRIEF WILL BE AUTOMATICALLY DISCARDED. FOLLOW THE INSTRUCTIONS!

Industry/Entity Type

Travel

Number of Pages Required

1 page

Font styles to use
Sans Serif

Colors

Designer to choose colors to be used in the design.

Requirements
Must have
• Follow wireframe and use content in wireframe (see Tavoni.io link)

```html
<!DOCTYPE html>
<html lang="en">
<head>
<meta charset="utf-8">
<title>SoarVane — Home</title>
<link rel="stylesheet" href="https://fonts.googleapis.com/css2?family=Barlow:wght@300;400;500;600&display=swap">
<style>
:root{
  --black:#000000;
  --ink:#2f2f2f;
  --mid:#5d5d5d;
  --soft:#a1a1a1;
  --mist:#e1e1e1;
  --white:#ffffff;
  --stage:#cccccc;
}
*{box-sizing:border-box;margin:0;padding:0}
html,body{width:1200px;height:4515px;overflow:hidden}
body{background:var(--stage);font-family:"Barlow",sans-serif;color:var(--white);position:relative}
.page{position:absolute;left:244px;top:292px;width:712px;height:4114px;background:var(--black);overflow:hidden}
.sec{position:relative;width:712px}
.card{position:absolute;left:8px;right:8px;top:0;bottom:0;background:linear-gradient(180deg,#1b1b1b,#111);border-radius:4px}
.pad{position:absolute;left:66px}
.eyebrow{font-size:7px;letter-spacing:2px;color:var(--mid);text-transform:uppercase}
h1,h2,h3{font-weight:500;line-height:1.12}
h1{font-size:37px;letter-spacing:-.3px}
h2{font-size:25px;letter-spacing:-.2px}
.grey{color:var(--soft)}
.body{font-size:8px;line-height:1.6;color:var(--mid);font-weight:400}
.btns{display:flex;gap:8px}
.btn{font-size:7px;padding:6px 12px;border:1px solid var(--mid);border-radius:2px;color:var(--white);display:inline-flex;align-items:center;gap:5px;white-space:nowrap}
.btn.solid{background:var(--white);color:var(--black);border-color:var(--white)}
.btn.ghost{border:none;padding-left:4px}

/* imagery placeholders: soft tonal gradients in the photo's own light */
.photo{position:absolute;border-radius:4px;overflow:hidden}
.photo.tarmac{background:
  radial-gradient(120% 60% at 30% 18%,#e8e8e8 0%,rgba(232,232,232,0) 70%),
  linear-gradient(180deg,#c9c9c9 0%,#9a9a9a 48%,#4a4a4a 62%,#6b6b6b 80%,#2b2b2b 100%)}
.photo.cabin{background:
  radial-gradient(70% 55% at 50% 45%,#f2f2f2 0%,rgba(242,242,242,0) 75%),
  linear-gradient(180deg,#8c8c8c 0%,#d9d9d9 35%,#bdbdbd 65%,#5e5e5e 100%)}
.photo.seat{background:
  radial-gradient(60% 70% at 60% 55%,#c4c4c4 0%,rgba(196,196,196,0) 70%),
  linear-gradient(160deg,#6f6f6f,#2e2e2e 70%,#151515)}
.photo.dusk{background:
  radial-gradient(90% 50% at 60% 35%,#9d9d9d 0%,rgba(157,157,157,0) 70%),
  linear-gradient(180deg,#5a5a5a 0%,#3a3a3a 55%,#161616 70%,#262626 100%)}
.photo.stairs{background:
  radial-gradient(60% 70% at 75% 40%,#f0f0f0 0%,rgba(240,240,240,0) 65%),
  linear-gradient(100deg,#1f1f1f 0%,#3c3c3c 40%,#a9a9a9 70%,#d4d4d4 100%)}
.photo.window{background:
  radial-gradient(40% 55% at 22% 35%,#ededed 0%,rgba(237,237,237,0) 70%),
  linear-gradient(120deg,#9b9b9b 0%,#5b5b5b 45%,#2a2a2a 100%)}
.photo.screen{background:
  radial-gradient(80% 40% at 50% 30%,#5e5e5e 0%,rgba(94,94,94,0) 75%),
  linear-gradient(180deg,#2c2c2c,#0f0f0f);border:3px solid #3a3a3a;border-bottom:none}
.photo.nose{background:
  radial-gradient(45% 40% at 62% 52%,#c7c7c7 0%,#6a6a6a 35%,rgba(30,30,30,0) 75%)}

/* nav */
.nav{height:40px;display:flex;align-items:center;padding:0 66px 0 66px;border-bottom:1px solid #151515}
.brand{font-size:13px;font-weight:400;color:var(--white);display:flex;align-items:center;gap:5px}
.brand i{width:7px;height:7px;background:var(--white);display:inline-block}
.nav .links{display:flex;gap:26px;margin-left:56px;font-size:6.5px;color:var(--soft)}
.nav .actions{margin-left:auto;display:flex;gap:6px}
.nav .actions span{font-size:6px;padding:5px 9px;border:1px solid var(--mid);border-radius:2px}
.nav .actions span.on{background:var(--ink)}
/* hero */
.hero{height:491px}
.hero h1{position:absolute;left:66px;top:76px;width:310px}
.hero .body{position:absolute;left:66px;top:213px;width:300px;font-size:7.5px}
.hero .btns{position:absolute;left:66px;top:256px}
.hero .fade{position:absolute;left:0;right:0;bottom:0;height:80px;background:linear-gradient(0deg,#000,transparent)}
/* checks */
.checks{list-style:none;display:flex;flex-direction:column;gap:8px;font-size:6.5px;color:var(--soft)}
.checks li{display:flex;align-items:center;gap:6px}
.checks svg{width:9px;height:9px}
/* options */
.opt{position:absolute;left:418px;width:230px}
.opt h3{font-size:14.5px;color:var(--soft)}
.opt p{font-size:7px;line-height:1.6;color:var(--mid);margin-top:6px}
.opt.active{border-left:2px solid var(--white);padding-left:8px;left:410px}
.opt.active h3{color:var(--white)}
.opt.active p{color:var(--mist)}
/* feature tiles */
.tile{position:absolute;width:134px;height:72px;background:#262626;border-radius:3px;padding:12px}
.tile b{font-size:9px;font-weight:500;display:block}
.tile p{font-size:6.5px;color:var(--mid);line-height:1.5;margin-top:5px}
/* services */
.svc{position:absolute;top:188px;width:170px}
.svc .ico{width:40px;height:40px;border-radius:4px;background:#2a2a2a;display:flex;align-items:center;justify-content:center}
.svc b{display:block;margin-top:18px;font-size:10px;font-weight:500}
.svc p{font-size:6.5px;color:var(--mid);line-height:1.5;margin-top:4px;width:150px}
/* testimonial */
.quote{text-align:center;padding-top:48px}
.stars{font-size:8px;letter-spacing:2px;color:var(--mid)}
.quote q{display:block;font-size:15px;line-height:1.35;margin-top:10px;quotes:"\201C" "\201D"}
.who{display:flex;justify-content:center;align-items:center;gap:8px;margin-top:18px}
.avatar{width:28px;height:28px;border-radius:50%;background:radial-gradient(circle at 50% 40%,#d0d0d0,#4a4a4a)}
.who b{font-size:7px;font-weight:500;display:block;text-align:left}
.who span{font-size:6px;color:var(--mid)}
/* partners */
.partners{position:absolute;left:60px;right:60px;top:92px;display:flex;flex-wrap:wrap;justify-content:center;gap:22px 48px}
.badge{width:58px;height:16px;border-radius:3px;background:#3a3a3a}
/* newsletter */
.field{display:flex;align-items:center;width:232px;height:30px;border:1px solid var(--ink);border-radius:3px;padding:0 4px 0 12px;font-size:7px;color:var(--mid)}
.field .btn{margin-left:auto}
/* faq */
.faq{position:absolute;left:56px;right:56px;top:130px;display:flex;flex-direction:column;gap:10px}
.q{border:1px solid #2c2c2c;border-radius:2px;padding:9px 22px;font-size:6.5px;display:flex;flex-wrap:wrap;justify-content:space-between;background:rgba(0,0,0,.3)}
.q p{flex-basis:100%;font-size:6px;color:var(--mid);line-height:1.6;margin-top:8px}
/* footer */
.foot{display:flex;padding:40px 66px 0 66px}
.foot .col{width:90px;font-size:6.5px;color:var(--mid);line-height:2.8}
.foot .col b{color:var(--white);font-weight:500;display:block;line-height:2}
.legal{position:absolute;left:66px;right:66px;top:160px;border-top:1px solid var(--ink);padding-top:20px;display:flex;gap:18px;font-size:6px;color:var(--mid)}
.social{margin-left:auto;display:flex;gap:8px}
.social i{width:6px;height:6px;background:var(--soft);display:block;border-radius:50%}
</style>
</head>
<body>
<main class="page">

  <header class="nav">
    <div class="brand">SoarVane <i></i></div>
    <nav class="links"><span>Aircraft</span><span>Programs</span><span>Why SoarVane</span><span>Lifestyle</span></nav>
    <div class="actions"><span class="on">Featured Blog</span><span>Article Title</span></div>
  </header>

  <section class="sec hero">
    <h1>Experience the Ultimate in <span class="grey">Luxury</span> Jet Travel</h1>
    <p class="body">SoarVane offers fractional jet ownership, jet card programs, private lease programs, all access programs, helicopter access programs and by the seat charter flights.</p>
    <div class="btns"><span class="btn solid">Explore →</span><span class="btn">Learn More →</span></div>
    <div class="photo tarmac" style="left:398px;top:0;width:130px;height:89px" role="img" aria-label="Passengers boarding a private jet at the airfield"></div>
    <div class="photo seat" style="left:545px;top:0;width:130px;height:128px" role="img" aria-label="Cream leather jet seat close up"></div>
    <div class="photo cabin" style="left:398px;top:107px;width:130px;height:164px" role="img" aria-label="Wide cream cabin interior of a large private jet"></div>
    <div class="photo seat" style="left:545px;top:145px;width:130px;height:165px" role="img" aria-label="Businessman relaxing in a cabin seat"></div>
    <div class="photo tarmac" style="left:398px;top:290px;width:130px;height:184px" role="img" aria-label="Traveller in a hat on the tarmac beside a jet"></div>
    <div class="photo tarmac" style="left:545px;top:327px;width:130px;height:150px" role="img" aria-label="Jet wing and engine on the apron"></div>
    <div class="fade"></div>
  </section>

  <section class="sec" style="height:394px">
    <div class="card" style="top:10px;bottom:10px"></div>
    <div class="pad" style="top:80px;width:300px">
      <p class="eyebrow">Discover</p>
      <h2 style="margin-top:6px">Experience the Luxury of Fractional Jet <span class="grey">Ownership</span></h2>
      <p class="body" style="margin-top:16px;font-size:7px">With SoarVane's fractional jet ownership program, you can enjoy the benefits of private jet travel without the hassle and expense of owning a whole aircraft. Our program offers flexibility, convenience and access to a fleet of luxurious jets, allowing you to travel in style and comfort.</p>
      <ul class="checks" style="margin-top:14px">
        <li><svg viewBox="0 0 10 10"><circle cx="5" cy="5" r="5" fill="#fff"/><path d="M2.8 5.2l1.5 1.5 3-3" stroke="#000" stroke-width="1.2" fill="none"/></svg>Flexible Ownership</li>
        <li><svg viewBox="0 0 10 10"><circle cx="5" cy="5" r="5" fill="#fff"/><path d="M2.8 5.2l1.5 1.5 3-3" stroke="#000" stroke-width="1.2" fill="none"/></svg>Easy Booking Process</li>
        <li><svg viewBox="0 0 10 10"><circle cx="5" cy="5" r="5" fill="#fff"/><path d="M2.8 5.2l1.5 1.5 3-3" stroke="#000" stroke-width="1.2" fill="none"/></svg>Luxurious Fleet</li>
      </ul>
      <div class="btns" style="margin-top:22px"><span class="btn">Learn More →</span><span class="btn ghost">Sign Up →</span></div>
    </div>
    <div class="photo tarmac" style="left:398px;top:62px;width:242px;height:280px" role="img" aria-label="Executive walking past a private jet on the runway"></div>
  </section>

  <section class="sec" style="height:350px">
    <div class="photo dusk" style="left:80px;top:52px;width:273px;height:142px" role="img" aria-label="Crew and passenger walking to a jet at dusk"></div>
    <div class="photo cabin" style="left:82px;top:212px;width:130px;height:84px" role="img" aria-label="Cabin seating area with couch"></div>
    <div class="photo cabin" style="left:223px;top:212px;width:130px;height:84px" role="img" aria-label="Cabin aisle with club seats"></div>
    <div class="opt active" style="top:72px"><h3>Flexible Ownership Options</h3><p>Choose from a variety of ownership programs and enjoy the freedom to fly on your own terms.</p></div>
    <div class="opt" style="top:146px"><h3>Convenient Jet Card Program</h3><p>Access a fleet of private jets with our exclusive jet card programs, offering flexibility and convenience.</p></div>
    <div class="opt" style="top:219px"><h3>Flexible Lease Programs</h3><p>Experience the luxury of private jet travel without the commitment with our flexible lease programs.</p></div>
  </section>

  <section class="sec" style="height:430px">
    <div class="card" style="top:0;bottom:8px"></div>
    <div class="pad" style="top:76px;width:300px">
      <p class="eyebrow">Experience</p>
      <h2 style="margin-top:6px">Unparallelled Luxury and <span class="grey">Convenience</span> for Private Aviation</h2>
      <p class="body" style="margin-top:14px;font-size:7px">Discover the ultimate in luxury and convenience with SoarVane. Our exclusive private aviation solutions provide you with unparalleled access to the world of private jets, ensuring seamless and extraordinary travel experiences.</p>
    </div>
    <div class="tile" style="left:66px;top:244px"><b>01 - Convenience</b><p>Enjoy hassle-free travel with flexible scheduling &amp; personalized services.</p></div>
    <div class="tile" style="left:214px;top:244px"><b>02 - Luxury</b><p>Enjoy hassle-free travel with flexible scheduling &amp; personalized services.</p></div>
    <div class="btns" style="position:absolute;left:66px;top:332px"><span class="btn solid">Learn More →</span><span class="btn ghost">Sign Up →</span></div>
    <div class="photo stairs" style="left:406px;top:74px;width:238px;height:294px" role="img" aria-label="Passenger on the phone stepping down the stairs of a private jet"></div>
  </section>

  <section class="sec" style="height:350px;background:linear-gradient(90deg,#000 35%,#141414)">
    <div class="photo nose" style="left:380px;top:0;width:332px;height:350px;border-radius:0" role="img" aria-label="Nose and cockpit of a private jet in dramatic light"></div>
    <div class="pad" style="top:44px;width:420px">
      <p class="eyebrow">Luxury</p>
      <h2 style="margin-top:6px;width:400px">Experience the Ultimate in Private Jet Travel</h2>
      <p class="body" style="margin-top:14px;width:410px;font-size:7px">SoarVane offers a wide range of exclusive services to meet your private jet travel needs. From fractional jet ownership to on-demand charter flights, we provide the highest level of luxury and convenience.</p>
    </div>
    <div class="svc" style="left:66px"><div class="ico"><svg width="16" height="16" viewBox="0 0 16 16"><rect x="3" y="2" width="10" height="12" rx="1" fill="none" stroke="#a1a1a1"/></svg></div><b>On-Demand Charter</b><p>Fly anywhere, anytime with our on-demand charter service.</p></div>
    <div class="svc" style="left:266px"><div class="ico"><svg width="16" height="16" viewBox="0 0 16 16"><circle cx="8" cy="8" r="6" fill="none" stroke="#a1a1a1"/><path d="M2 8h12M8 2v12" stroke="#a1a1a1"/></svg></div><b>Global Response</b><p>We provide specialized medical transportation services worldwide.</p></div>
    <div class="svc" style="left:476px"><div class="ico"><svg width="16" height="16" viewBox="0 0 16 16"><path d="M2 9l12-3-2 4z" fill="#a1a1a1"/></svg></div><b>Fractional Jet Ownership</b><p>Enjoy the benefits of owning a private jet without the hassles.</p></div>
    <div class="btns" style="position:absolute;left:66px;top:304px"><span class="btn">Learn More →</span><span class="btn ghost">Sign Up →</span></div>
  </section>

  <section class="sec" style="height:326px">
    <div class="card" style="top:30px;bottom:0"></div>
    <div class="pad" style="top:84px;width:330px">
      <h2>Experience luxury travel like never before</h2>
      <p class="body" style="margin-top:12px;font-size:7px">Contact us today to book your exclusive private jet experience.</p>
    </div>
    <div class="btns" style="position:absolute;right:66px;top:86px"><span class="btn solid" style="background:#e1e1e1">Learn More →</span><span class="btn">Sign Up →</span></div>
    <div class="photo screen" style="left:295px;top:142px;width:140px;height:184px;border-radius:18px 18px 0 0" role="img" aria-label="Phone showing the SoarVane membership app"></div>
  </section>

  <section class="sec quote" style="height:206px">
    <p class="stars">★★★★★</p>
    <q>SoarVane's services have exceeded my expectations.<br>The convenience and luxury of flying with them is unmatched.</q>
    <div class="who"><div class="avatar" role="img" aria-label="Client portrait"></div><div><b>Lucas Verne</b><span>CEO, Northwind Co</span></div></div>
  </section>

  <section class="sec" style="height:212px">
    <div class="card" style="top:0;bottom:8px"></div>
    <p style="position:absolute;top:54px;width:100%;text-align:center;font-size:11px">Trusted by top-tier companies and brands around the globe</p>
    <div class="partners">
      <span class="badge"></span><span class="badge"></span><span class="badge"></span><span class="badge"></span><span class="badge"></span><span class="badge"></span>
      <span class="badge"></span><span class="badge"></span><span class="badge"></span>
    </div>
  </section>

  <section class="sec" style="height:272px">
    <div class="pad" style="top:36px;width:300px">
      <h2>Subscribe to Our <span class="grey">Newsletter</span></h2>
      <p class="body" style="margin-top:14px;font-size:7px">Stay updated with exclusive offers and aircraft industry news.</p>
      <div class="field" style="margin-top:20px">Enter Your Email Address<span class="btn solid">Join SoarVane Now →</span></div>
      <p style="font-size:6px;color:var(--soft);margin-top:10px">By joining, you agree with our Terms and Conditions</p>
    </div>
    <div class="photo window" style="left:410px;top:24px;width:234px;height:168px" role="img" aria-label="Traveller holding a phone beside a cabin window"></div>
  </section>

  <section class="sec" style="height:520px">
    <div class="card" style="top:0;bottom:20px;background:
      radial-gradient(60% 30% at 50% 78%,#4a4a4a 0%,rgba(74,74,74,0) 80%),
      linear-gradient(180deg,#1c1c1c 50%,#303030 78%,#141414)" role="img" aria-label="Dimmed jet cabin interior behind the questions"></div>
    <div class="pad" style="top:40px"><h2>Frequently</h2><p class="body" style="margin-top:18px;font-size:7px">Find answers to common questions about SoarVane's services and programs.</p></div>
    <div class="faq">
      <div class="q">What is SoarVane?<span>+</span></div>
      <div class="q">How it Works?<span>−</span><p>SoarVane works by allowing customers to purchase fractional ownership of a private jet, join jet card programs or set a number of flight hours, lease a private jet for specific periods, or access our all access and helicopter programs. We also offer charter flights where customers can book individual seats on a private jets.</p></div>
      <div class="q">Why Choose SoarVane?<span>+</span></div>
      <div class="q">How to Book?<span>+</span></div>
      <div class="q">What are the Benefits?<span>+</span></div>
    </div>
    <div class="pad" style="top:380px">
      <h3 style="font-size:13px">Still have questions?</h3>
      <p class="body" style="margin-top:4px;font-size:7px">Contact us for more information.</p>
      <span class="btn solid" style="margin-top:14px">Contact →</span>
    </div>
  </section>

  <section class="sec" style="height:296px">
    <div class="card" style="top:0;bottom:0;background:#0b0b0b"></div>
    <div class="pad" style="top:44px;width:300px"><h2>Experience luxury travel like never before</h2></div>
    <p class="body" style="position:absolute;left:404px;top:46px;width:250px;font-size:6.5px">Discover the ultimate in private jet travel with SoarVane. Whether you're looking for fractional ownership, jet card programs, private jet lease programs, all access programs, helicopter access programs, or by-the-seat charter flights, we have the perfect solution for your travel needs.</p>
    <div class="btns" style="position:absolute;left:404px;top:110px"><span class="btn solid" style="background:#e1e1e1">Book Today →</span><span class="btn">Contact →</span></div>
    <div class="photo screen" style="left:200px;top:156px;width:112px;height:140px;border-radius:16px 16px 0 0" role="img" aria-label="Phone showing SoarVane app home screen"></div>
    <div class="photo screen" style="left:270px;top:180px;width:112px;height:116px;border-radius:16px 16px 0 0" role="img" aria-label="Second phone showing SoarVane app hero screen"></div>
  </section>

  <footer class="sec" style="height:237px">
    <div class="foot">
      <div class="brand" style="width:112px;align-self:flex-start">SoarVane <i></i></div>
      <div class="col"><b>About Us</b>Charter<br>Fleet<br>Destinations<br>Pricing<br>Contact</div>
      <div class="col"><b>Services</b>Private Jets<br>Helicopters<br>Jet Cards<br>Membership<br>FAQ</div>
      <div class="col"><b>Terms</b>Privacy<br>Careers<br>Press<br>Blog<br>Support</div>
      <div style="margin-left:20px">
        <b style="font-size:7px;font-weight:500">Subscribe</b>
        <div class="field" style="margin-top:12px;width:174px;height:26px;font-size:6px">Enter Email Address<span class="btn solid" style="font-size:6px">Join SoarVane Now →</span></div>
        <p style="font-size:5px;color:var(--soft);margin-top:8px">By subscribing, you agree to our Privacy Policy and consent to receive updates.</p>
      </div>
    </div>
    <div class="legal"><span>Copyright © 2024 SoarVane. All Rights Reserved.</span><span>Privacy Policy</span><span>Terms of Service</span><span>Cookie Settings</span>
      <div class="social"><i></i><i></i><i></i><i></i></div></div>
  </footer>

</main>
</body>
</html>
```